Business card

I have changed logo's and colors. I have uploaded the new logo and colors.

In my head I am thinking about the main logo and text beside logo to be on one side of the card. The other side of the card to have just my picture and contact information.

The "R" emblem and the "equal housing" emblem... cut he MLS from the "R". and remove the wording from the house emblem.

Info on Card:

Wes Trundell
Designated Broker, CDPE, CNE, GRI
Direct: 602.555.0143
Fax: 623.555.0198
Wes@TrundellandAssociates.example
www.TrundellandAssociates.example
4193 North Sagebend Lane Glendale, AZ 85308

Please see brief as I have uploaded a new logo and a few notes.

Reason: I changed the logo and colors. Please see brief

I am leaning towards maybe a black business card(or at least on the front where the logo is). I liked several designs that were submitted. Please re-submit.

House

```html
<!DOCTYPE html>
<html lang="en">
<head>
<meta charset="utf-8">
<title>Trundell &amp; Associates – Business Card</title>
<link href="https://fonts.googleapis.com/css2?family=Cinzel:wght@500&family=Questrial&display=swap" rel="stylesheet">
<style>
  :root {
    --page-bg: #d9d4cc;
    --card-black: #050505;
    --accent-orange: #f08a2c;
    --text-teal: #9fc7cc;
    --frame-orange: #f26a21;
    --photo-light: #e9ecee;
    --photo-dark: #3a4048;
    --mark-teal: #7fb3bb;
    --icon-white: #ffffff;
  }
  * { box-sizing: border-box; margin: 0; padding: 0; }
  html, body {
    width: 1200px; height: 870px; overflow: hidden;
    background: var(--page-bg);
  }
  .canvas {
    position: relative; width: 1200px; height: 870px;
    display: flex; justify-content: center; align-items: center; gap: 80px;
  }
  .card {
    position: relative; width: 440px; height: 770px;
    background: var(--card-black);
    box-shadow: 0 6px 18px rgba(0,0,0,0.25);
    font-family: "Questrial", "Century Gothic", sans-serif;
    color: var(--text-teal);
  }

  /* Front */
  .brand {
    position: absolute; top: 92px; left: 40px; right: 30px;
    display: flex; align-items: center; gap: 18px;
  }
  .brand-mark {
    width: 92px; height: 92px; border-radius: 50%;
    background: var(--mark-teal); flex: none;
  }
  .brand-name {
    font-family: "Cinzel", serif; font-weight: 500;
    color: var(--accent-orange); font-size: 30px; line-height: 1.15;
    letter-spacing: 1px;
  }
  .identity {
    position: absolute; top: 300px; left: 0; right: 0; text-align: center;
  }
  .person-name {
    font-family: "Cinzel", serif; font-weight: 500;
    color: var(--accent-orange); font-size: 38px; letter-spacing: 1px;
  }
  .person-title { font-size: 26px; margin-top: 2px; }
  .person-credentials { font-size: 21px; margin-top: 4px; }
  .contact {
    position: absolute; top: 545px; left: 0; right: 0;
    text-align: center; font-size: 24px;
  }
  .contact-line { margin-bottom: 14px; }
  .contact-label { color: var(--accent-orange); margin-right: 6px; }
  .address { margin-top: 26px; line-height: 1.3; }

  /* Back */
  .portrait {
    position: absolute; top: 70px; left: 50%; transform: translateX(-50%);
    width: 250px; height: 290px; border-radius: 50%;
    border: 8px solid var(--frame-orange);
    background: radial-gradient(ellipse at 50% 35%, var(--photo-light) 45%, var(--photo-dark) 100%);
  }
  .web-contact {
    position: absolute; top: 470px; left: 0; right: 0;
    text-align: center; font-size: 20px; line-height: 1.7;
  }
  .housing-badge {
    position: absolute; right: 50px; bottom: 50px;
    width: 66px; height: 66px;
  }
</style>
</head>
<body>
<main class="canvas">
  <section class="card card-front">
    <div class="brand">
      <span class="brand-mark"></span>
      <span class="brand-name">Trundell &amp; Associates</span>
    </div>
    <div class="identity">
      <p class="person-name">Wes Trundell</p>
      <p class="person-title">Designated Broker</p>
      <p class="person-credentials">CDPE, CNE, GRI</p>
    </div>
    <div class="contact">
      <p class="contact-line"><span class="contact-label">T</span>: 602.555.0143</p>
      <p class="contact-line"><span class="contact-label">F</span>: 623.555.0198</p>
      <p class="address">4193 North Sagebend Lane Glendale,<br>AZ 85308</p>
    </div>
  </section>

  <section class="card card-back">
    <div class="portrait" role="img" aria-label="Portrait photo of Wes Trundell in a dark suit"></div>
    <div class="web-contact">
      <p>Wes@TrundellandAssociates.example</p>
      <p>www.TrundellandAssociates.example</p>
    </div>
    <svg class="housing-badge" viewBox="0 0 66 66" aria-hidden="true">
      <rect x="4" y="4" width="58" height="58" fill="none" stroke="var(--icon-white)" stroke-width="5"/>
    </svg>
  </section>
</main>
</body>
</html>
```